KeyHarbor needs a modern business card

We are a modern conveyancing company and we need to appeal to the top (Multi-million dollar properties)and bottom on the property conveyancing market but our sweet spot is the middle of the market. I like professional with a hint of unconventional.

Target Market(s)

As above

Industry/Entity Type

Real Estate

Contact Information for Business Card

Back Of card:
thinking black with the logo and a tag line (I could be wrong about the black)
Tag line - Sound Advice, Seamless Settlement

Front of Card:
Marissa Toll (BBus (Finance) LLB)
Licensed Conveyancer
Email: marissa@keyharbor.com.au

Key Harbor
ABN: 48 913 706
Suite 14, Level 3, 9 Calloway Road Lindhurst Park, NSW 2178
Phone: 1300 682 917

Sydney - Melbourne - Brisbane (Perhaps have this along the bottom of the card)

Requirements
Must have
• Sleek, modern and top end appeal (But approachable)
Should not have
• Not too cluttered

```html
<!DOCTYPE html>
<html lang="en">
<head>
<meta charset="utf-8">
<title>KeyHarbor Business Card</title>
<link href="https://fonts.googleapis.com/css2?family=Exo+2:wght@300;400;600&display=swap" rel="stylesheet">
<style>
  :root {
    --page-bg: #e9e8e4;
    --card-white: #ffffff;
    --ink-dark: #3f4144;
    --ink-mid: #5c5f63;
    --rule-navy: #2c4a6e;
    --accent-green: #3fae3a;
    --accent-blue: #2f5c8f;
    --back-top: #55585d;
    --back-bottom: #2e3034;
    --tagline: #d9dbde;
  }
  * { box-sizing: border-box; margin: 0; padding: 0; }
  html, body {
    width: 1200px; height: 1023px; overflow: hidden;
    background: var(--page-bg);
    font-family: "Exo 2", "Segoe UI", sans-serif;
  }
  .sheet {
    width: 1200px; height: 1023px;
    display: flex; flex-direction: column; align-items: center; justify-content: center;
    gap: 60px;
  }
  .card {
    width: 700px; height: 400px;
    border-radius: 4px;
    box-shadow: 0 10px 28px rgba(0,0,0,.18);
    position: relative; overflow: hidden;
  }

  /* Front */
  .card-front { background: var(--card-white); color: var(--ink-dark); }
  .front-brand {
    position: absolute; left: 40px; top: 34px;
    font-size: 56px; font-weight: 400; letter-spacing: -1px; color: var(--ink-dark);
  }
  .rule { position: absolute; height: 1.5px; background: var(--rule-navy); }
  .rule-top { left: 40px; right: 40px; top: 112px; }
  .rule-bottom { left: 40px; right: 40px; top: 318px; }
  .abn {
    position: absolute; right: 40px; top: 120px;
    font-size: 15px; color: var(--accent-blue); letter-spacing: .5px;
  }
  .person { position: absolute; right: 40px; top: 156px; text-align: right; }
  .person-name {
    display: flex; align-items: center; justify-content: flex-end; gap: 12px;
    font-size: 30px; font-weight: 400; color: var(--accent-green);
  }
  .person-badge { width: 30px; height: 30px; border-radius: 50%; background: var(--accent-green); }
  .person-role, .person-quals {
    font-size: 16px; font-weight: 300; color: var(--ink-mid); margin-right: 42px; line-height: 1.3;
  }
  .address {
    position: absolute; right: 40px; top: 262px; text-align: right;
    font-size: 15px; font-weight: 300; color: var(--ink-mid); line-height: 1.35;
  }
  .contacts {
    position: absolute; left: 40px; top: 330px;
    font-size: 16px; font-weight: 300; color: var(--ink-mid); line-height: 1.6;
  }
  .contact-row { display: flex; align-items: center; gap: 10px; }
  .contact-icon { width: 16px; height: 16px; flex: none; }

  /* Back */
  .card-back {
    background: radial-gradient(ellipse at 55% 40%, var(--back-top), var(--back-bottom) 80%);
    display: flex; align-items: center; justify-content: center;
  }
  .back-lockup { display: flex; align-items: center; gap: 22px; }
  .back-mark { width: 70px; height: 70px; background: var(--accent-green); }
  .back-brand {
    font-size: 64px; font-weight: 400; color: #ffffff; letter-spacing: -1px; line-height: 1;
  }
  .back-tagline {
    font-size: 17px; font-weight: 300; color: var(--tagline); margin-top: 8px; letter-spacing: .3px;
  }
</style>
</head>
<body>
<main class="sheet">

  <section class="card card-front" aria-label="Business card front">
    <div class="front-brand">KeyHarbor</div>
    <div class="rule rule-top"></div>
    <div class="abn">ABN: 48 913 706</div>

    <div class="person">
      <div class="person-name">Marissa Toll <span class="person-badge"></span></div>
      <div class="person-role">Licensed Conveyancer</div>
      <div class="person-quals">BBus (Finance) LLB</div>
    </div>

    <div class="address">
      Suite 14, Level 3,<br>
      9 Calloway Road Lindhurst Park, NSW 2178
    </div>
    <div class="rule rule-bottom"></div>

    <div class="contacts">
      <div class="contact-row">
        <svg class="contact-icon" viewBox="0 0 16 16" aria-hidden="true">
          <circle cx="8" cy="8" r="8" fill="#3fae3a"/>
          <path d="M5.2 4.2l1.6-.4.9 2-1 .8a5 5 0 0 0 2.7 2.7l.8-1 2 .9-.4 1.6c-3.7.2-6.8-2.9-6.6-6.6z" fill="#fff"/>
        </svg>
        1300 682 917
      </div>
      <div class="contact-row">
        <svg class="contact-icon" viewBox="0 0 16 16" aria-hidden="true">
          <rect x="0" y="3" width="16" height="11" rx="1" fill="#3fae3a"/>
          <path d="M1 4l7 5 7-5" fill="none" stroke="#fff" stroke-width="1.4"/>
        </svg>
        marissa@keyharbor.com.au
      </div>
    </div>
  </section>

  <section class="card card-back" aria-label="Business card back">
    <div>
      <div class="back-lockup">
        <span class="back-mark"></span>
        <span class="back-brand">KeyHarbor</span>
      </div>
      <div class="back-tagline">Sound Advice, Seamless Settlement</div>
    </div>
  </section>

</main>
</body>
</html>
```